Header Design

I would like a new header design for my website - www.nestmarlo.com.

I am a Realtor and the header should reflect that and complement the theme.

The attached logo needs to be included and the information that is already there. Also, the colors need to match.

Marlo Quinby
Connecting you to the Los Angeles real estate scene.

Industry/Entity Type

Realtor

```html
<!DOCTYPE html>
<html lang="en">
<head>
<meta charset="utf-8">
<title>Marlo Quinby — Website Header</title>
<link rel="stylesheet" href="https://fonts.googleapis.com/css2?family=Cinzel:wght@400&family=Ubuntu:wght@400&display=swap">
<style>
  :root {
    --gold: #c7b166;
    --plum: #472e50;
    --plum-deep: #3b2843;
    --ink: #4a3152;
    --backdrop: #eeeeee;
    --ivory: #ffffff;
  }
  * { box-sizing: border-box; margin: 0; padding: 0; }
  html, body {
    width: 1200px;
    height: 1000px;
    overflow: hidden;
  }
  body {
    background: var(--backdrop);
    position: relative;
  }
  .site-header {
    position: absolute;
    left: 66px;
    top: 445px;
    width: 1068px;
    height: 111px;
  }
  .site-header > * { position: absolute; }
  .accent-bar {
    left: 0; top: 0;
    width: 37px; height: 111px;
    background: var(--gold);
  }
  .brand-square {
    left: 41px; top: 0;
    width: 105px; height: 111px;
    background: var(--plum-deep);
  }
  .brand-name {
    left: 151px; top: 0;
    width: 399px; height: 111px;
    background: var(--plum);
    display: flex;
    align-items: center;
    justify-content: center;
    color: var(--ivory);
    font-family: "Cinzel", serif;
    font-weight: 400;
    font-size: 48px;
    letter-spacing: 1px;
    padding-top: 4px;
  }
  .tagline-panel {
    left: 557px; top: 0;
    width: 511px; height: 78px;
    background: var(--gold);
    display: flex;
    align-items: center;
    justify-content: center;
    color: var(--ink);
    font-family: "Ubuntu", sans-serif;
    font-size: 18.5px;
    padding-top: 6px;
  }
  .base-bar {
    left: 557px; top: 84px;
    width: 511px; height: 27px;
    background: var(--plum);
  }
</style>
</head>
<body>
  <header class="site-header">
    <div class="accent-bar"></div>
    <div class="brand-square"></div>
    <h1 class="brand-name">Marlo Quinby</h1>
    <p class="tagline-panel">Connecting you to the Los Angeles real estate scene.</p>
    <div class="base-bar"></div>
  </header>
</body>
</html>
```